Letter Head, for use on daily correspondence with other companies

Hi

I want a professional Letter head, That my company can use to corresponded with other companies we do business with on a daily basis.

I want this done as soon as possible as this is peak session for us.

I have attached the company logo so please be creative and professional.
Kind regards

Osric

Target Market(s)

All Audience searching for tickets, people in the entertainment world

Industry/Entity Type

Entertainment Industry

Font styles to use
Serif
Sans Serif
Decorative
Script

Requirements
Must have
• Very professional image.
• I will know want i want when i see it
• so please do your utmost in your professional standards
• Address of the company 47 marlow lane, telephone number 0207 581 2937
• Vat number: 486 2917 58.
• This letter head my be able to acomodate usage for directors & CEO as well as managers and employess
Nice to have
• A great professional image
Should not have
• Be creative please

```html
<!DOCTYPE html>
<html lang="en">
<head>
<meta charset="utf-8">
<title>Kestrel Letterhead</title>
<link rel="stylesheet" href="https://fonts.googleapis.com/css2?family=Montserrat:wght@400;700&family=Tinos:wght@400;700&display=swap">
<style>
  :root {
    --backdrop: #e3d8c4;
    --paper: #ffffff;
    --brand-red: #c8220e;
    --brand-fade: #f4d6d2;
    --body-ink: #5a5a5a;
    --rule: #9a9a9a;
    --footer-ink: #333333;
    --seal-blue: #6f8fd0;
  }
  * { box-sizing: border-box; margin: 0; padding: 0; }
  html, body {
    width: 1200px; height: 900px; overflow: hidden;
    background: var(--backdrop);
  }
  .letterhead {
    position: absolute;
    left: 300px; top: 26px;
    width: 600px; height: 848px;
    background: var(--paper);
    box-shadow: 0 6px 24px rgba(0,0,0,0.12);
    font-family: "Montserrat", sans-serif;
  }
  .brand-edge {
    position: absolute; left: 0; top: 0;
    width: 9px; height: 100%;
    background: linear-gradient(to bottom, var(--brand-red) 0%, var(--brand-red) 45%, var(--brand-fade) 92%, var(--paper) 100%);
  }
  .brand-block {
    position: absolute; left: 42px; top: 40px;
    width: 112px; height: 92px;
    background: var(--brand-red);
    display: flex; align-items: center; justify-content: center;
  }
  .brand-name {
    color: #ffffff;
    font-family: "Montserrat", sans-serif;
    font-weight: 700;
    font-size: 21px;
    letter-spacing: 0.5px;
  }
  .letter-body {
    position: absolute; left: 110px; top: 232px;
    width: 420px;
    color: var(--body-ink);
    font-size: 9.6px;
    line-height: 1.75;
  }
  .letter-body p { margin-bottom: 17px; }
  .letter-body p:last-child { margin-bottom: 0; }
  .sign-off {
    position: absolute; left: 440px; top: 548px;
    width: 100px; text-align: center;
    color: var(--body-ink); font-size: 9.6px;
    line-height: 1.2;
  }
  .seal { display: block; margin: 5px auto 0; }
  .footer-rule {
    position: absolute; left: 60px; right: 40px; height: 1px;
    background: var(--rule);
  }
  .footer-rule--top { top: 650px; }
  .footer-rule--bottom { top: 790px; }
  .contact-line {
    position: absolute; left: 0; right: 0; top: 730px;
    text-align: center;
    font-family: "Tinos", serif;
    font-weight: 700;
    font-size: 13px;
    color: var(--footer-ink);
    line-height: 1.25;
  }
  .contact-line .gap { display: inline-block; width: 22px; }
</style>
</head>
<body>
  <main class="letterhead">
    <div class="brand-edge"></div>
    <div class="brand-block"><span class="brand-name">Kestrel</span></div>

    <section class="letter-body">
      <p>Lorem ipsum dolor sit amet, consectetur adipiscing elit. Donec orci purus, luctus vitae dignissim eu, iaculis sed purus. Vivamus faucibus, ipsum nec aliquet viverra, leo mauris condimentum ligula, sit amet sagittis enim ligula quis arcu. Nam egestas tortor id nisi porttitor mattis. In tortor ante, ultricies in suscipit a, tempus non massa. Vivamus et auctor mi. Fusce vel massa nulla. Phasellus nec eros mauris, et scelerisque orci.</p>
      <p>Donec malesuada orci vitae nulla accumsan porta a id massa. Quisque accumsan iaculis magna sit amet fringilla. Maecenas consequat, magna eget tincidunt semper, odio nibh rutrum mi, id feugiat ante nisi eu risus. Vestibulum nunc orci, rhoncus a placerat in, ultricies in mi. Cras mattis varius eros, vel fringilla nisi suscipit eget. Quisque scelerisque sagittis nulla at porttitor.</p>
      <p>Sed id augue vitae urna euismod commodo aliquet a quam. Pellentesque arcu velit, cursus et malesuada ut, consequat et diam. Nullam erat sem, rhoncus id ullamcorper vitae, rhoncus et arcu. In ultricies ultricies nulla, ut rutrum nisi iaculis at. Donec eu magna a metus ornare faucibus. Fusce aliquet faucibus ultricies. Morbi semper, est id tincidunt gravida, sem arcu adipiscing lacus, ac bibendum nulla leo eu purus. Quisque nec diam sed risus consectetur accumsan quis quis nibh. Vestibulum id purus lorem.</p>
    </section>

    <div class="sign-off">
      Sincerely,
      <svg class="seal" width="62" height="62" viewBox="0 0 72 72" role="img" aria-label="Signature over an official seal">
        <circle cx="36" cy="36" r="33" fill="none" stroke="var(--seal-blue)" stroke-width="2"/>
        <circle cx="36" cy="36" r="22" fill="none" stroke="var(--seal-blue)" stroke-width="1"/>
        <rect x="14" y="30" width="44" height="12" fill="#d8d8d8" opacity="0.7"/>
      </svg>
    </div>

    <div class="footer-rule footer-rule--top"></div>
    <div class="contact-line">
      47 marlow lane<span class="gap"></span>Tel: 0207 581 2937<br>
      Vat: 486 2917 58
    </div>
    <div class="footer-rule footer-rule--bottom"></div>
  </main>
</body>
</html>
```